Sumvane financial services stationery design

We need business stationery designed with letterheads, business cards, with compliments and envelope for a business that offers tax and accounting services

Designs look the same

Target Market(s)

Small to medium businesses, individuals, Self managed superfunds

Industry/Entity Type

Business

Font styles to use
Serif
Other font styles liked:
• Atlanta

Colors
32a6d6
3277b5

Requirements
Must have
• Logo incorporated with all my stationery
• professional
Should not have
• Lots of colours
• Busy

```html
<!DOCTYPE html>
<html lang="en">
<head>
<meta charset="utf-8">
<title>Sumvane Financial Services – Stationery</title>
<link href="https://fonts.googleapis.com/css2?family=Cinzel:wght@400&family=Lato:wght@400;700&display=swap" rel="stylesheet">
<style>
  :root{
    --bg:#5f606b;
    --paper:#ffffff;
    --env:#eeeff1;
    --ink:#3d3e42;
    --mark-grey:#58595b;
    --band:#4d4e52;
    --blue:#1b75bb;
    --blue-light:#32a6d6;
    --card-dark:#4f5053;
  }
  *{box-sizing:border-box;margin:0;padding:0}
  html,body{width:1200px;height:960px;overflow:hidden}
  body{background:var(--bg);font-family:"Lato",Arial,sans-serif;color:var(--ink);position:relative}

  .sheet{position:absolute;background:var(--paper);overflow:hidden}

  /* brand lockup */
  .brand{position:absolute;display:flex;align-items:center;gap:6px}
  .brand__square{background:linear-gradient(135deg,var(--blue-light),var(--blue));flex:none}
  .brand__text{display:flex;flex-direction:column;line-height:1}
  .brand__name{font-family:"Cinzel",Georgia,serif;font-weight:400;color:var(--mark-grey);letter-spacing:.5px}
  .brand__sub{font-family:"Cinzel",Georgia,serif;color:var(--mark-grey);letter-spacing:1.6px;margin-top:2px}
  .brand--white .brand__name,.brand--white .brand__sub{color:#fff}

  /* contact lists */
  .contact{position:absolute;font-size:5px;line-height:7px;color:var(--ink)}
  .contact li{list-style:none;display:flex;align-items:center;gap:3px}
  .contact .gap{margin-top:3px}
  .icon{width:4px;height:4px;fill:var(--blue);flex:none}

  /* footer band */
  .footer{position:absolute;left:0;right:0;bottom:0}
  .footer__grey{position:absolute;left:0;right:0;bottom:0;background:var(--band)}
  .footer__blue{position:absolute;right:0;bottom:0;background:var(--blue);clip-path:polygon(9px 0,100% 0,100% 100%,0 100%);color:#fff;font-size:6px;display:flex;align-items:center;justify-content:center}

  /* envelope */
  .envelope{left:62px;top:232px;width:384px;height:268px;background:transparent;overflow:visible}
  .envelope__flap{position:absolute;left:0;top:0;width:384px;height:75px;background:#4a4b50;clip-path:polygon(3% 8%,8% 0,92% 0,97% 8%,100% 100%,0 100%)}
  .envelope__body{position:absolute;left:0;top:74px;width:384px;height:194px;background:linear-gradient(180deg,#f3f4f6,#e4e5e8)}

  /* letterhead */
  .letterhead{left:498px;top:230px;width:374px;height:504px}
  .letterhead__contact{left:276px;top:32px;padding-left:7px;border-left:1px solid #999}
  .letter{position:absolute;left:50px;width:272px;font-size:6px;line-height:9.5px;color:#444}
  .letter__date{top:127px}
  .letter__address{top:144px;line-height:7.6px}
  .letter__body{top:195px;text-align:justify}
  .letter__body p+p{margin-top:9px}
  .letter__sign{top:374px}
  .letter__sign strong{display:block;font-weight:400;font-size:8.5px;color:#333;margin-bottom:3px}

  /* compliments */
  .compliments{left:61px;top:531px;width:383px;height:193px}

  /* business cards */
  .card{width:211px;height:120px}
  .card--front{left:917px;top:230px}
  .card--back{left:918px;top:382px;background:var(--card-dark)}
  .card__name{position:absolute;left:13px;top:62px;font-size:8.5px;font-weight:700;color:var(--blue)}
  .card__role{position:absolute;left:13px;top:73px;font-size:4.6px;color:#333}
  .card__rule{position:absolute;left:52px;right:14px;top:76px;height:1px;background:#999}
  .card__address{position:absolute;right:14px;top:92px;font-size:4.6px;line-height:6.5px;text-align:right}
</style>
</head>
<body>
<svg width="0" height="0" style="position:absolute">
  <defs>
    <symbol id="i-phone" viewBox="0 0 10 10"><path d="M2 0l2 2-1 1.5c.8 1.5 2 2.7 3.5 3.5L8 6l2 2-1.5 2C4 9.5.5 6 0 1.5z"/></symbol>
    <symbol id="i-mobile" viewBox="0 0 10 10"><rect x="2.5" y="0" width="5" height="10" rx="1"/></symbol>
    <symbol id="i-mail" viewBox="0 0 10 10"><rect x="0" y="2" width="10" height="6" rx="1"/></symbol>
  </defs>
</svg>

<!-- Envelope -->
<section class="sheet envelope" aria-label="Envelope">
  <div class="envelope__flap"></div>
  <div class="envelope__body">
    <div class="brand" style="left:19px;top:19px">
      <span class="brand__square" style="width:30px;height:30px"></span>
      <span class="brand__text"><span class="brand__name" style="font-size:20px">Sumvane</span><span class="brand__sub" style="font-size:5.4px">Financial Services</span></span>
    </div>
    <ul class="contact" style="left:19px;top:135px">
      <li>Addres street, demo place</li>
      <li>P.O. Box 000, 888 Avenue</li>
      <li class="gap"><svg class="icon"><use href="#i-phone"/></svg>000-0000-0000</li>
      <li><svg class="icon"><use href="#i-mobile"/></svg>000-0000-0000</li>
      <li><svg class="icon"><use href="#i-mail"/></svg>info@sumvane-fs.com</li>
    </ul>
    <div class="footer" style="height:14px">
      <div class="footer__grey" style="height:9px"></div>
      <div class="footer__blue" style="width:118px;height:14px">www.sumvane-fs.com</div>
    </div>
  </div>
</section>

<!-- Compliments slip -->
<section class="sheet compliments" aria-label="With compliments slip">
  <div class="brand" style="left:20px;top:20px">
    <span class="brand__square" style="width:30px;height:30px"></span>
    <span class="brand__text"><span class="brand__name" style="font-size:20px">Sumvane</span><span class="brand__sub" style="font-size:5.4px">Financial Services</span></span>
  </div>
  <ul class="contact" style="left:20px;top:135px">
    <li>Addres street, demo place</li>
    <li>P.O. Box 000, 888 Avenue</li>
    <li class="gap"><svg class="icon"><use href="#i-phone"/></svg>000-0000-0000</li>
    <li><svg class="icon"><use href="#i-mobile"/></svg>000-0000-0000</li>
    <li><svg class="icon"><use href="#i-mail"/></svg>info@sumvane-fs.com</li>
  </ul>
  <div class="footer" style="height:16px">
    <div class="footer__grey" style="height:10px"></div>
    <div class="footer__blue" style="width:118px;height:16px">www.sumvane-fs.com</div>
  </div>
</section>

<!-- Letterhead -->
<section class="sheet letterhead" aria-label="Letterhead">
  <div class="brand" style="left:30px;top:31px">
    <span class="brand__square" style="width:34px;height:34px"></span>
    <span class="brand__text"><span class="brand__name" style="font-size:22px">Sumvane</span><span class="brand__sub" style="font-size:5.6px">Financial Services</span></span>
  </div>
  <ul class="contact letterhead__contact">
    <li>Addres street, demo place</li>
    <li>P.O. Box 000, 888 Avenue</li>
    <li class="gap"><svg class="icon"><use href="#i-phone"/></svg>000-0000-0000</li>
    <li><svg class="icon"><use href="#i-mobile"/></svg>000-0000-0000</li>
    <li><svg class="icon"><use href="#i-mail"/></svg>info@sumvane-fs.com</li>
  </ul>

  <p class="letter letter__date">February 05, 2018</p>
  <p class="letter letter__address">Dear Ms. Halvey,<br>demo street,<br>demo placeP.O.<br>Box 000, 555 Avenue</p>
  <div class="letter letter__body">
    <p>Lorem ipsum dolor sit amet, consectetur adipiscing elit. Donec orci purus, luctus vitae dignissim eu, iaculis sed purus. Vivamus faucibus, ipsum nec aliquet viverra, leo mauris condimentum ligula, sit amet sagittis enim ligula quis arcu. Nam egestas tortor id nisi porttitor mattis. In tortor ante, ultricies in suscipit a, tempus non massa. Vivamus et auctor mi. Fusce vel massa nulla. Phasellus nec eros mauris, et scelerisque orci. Donec malesuada orci vitae nulla accumsan porta a id massa. Quisque accumsan iaculis magna sit amet fringilla. Maecenas consequat, magna eget tincidunt semper, odio nibh rutrum mi, id feugiat ante nisi eu risus. Vestibulum nunc orci, rhoncus a placerat in, ultricies in mi. Cras mattis varius eros, vel fringilla nisi suscipit eget.</p>
    <p>Quisque scelerisque sagittis nulla at porttitor. Mauris a justo et tellus interdum tristique. Sed id augue vitae urna euismod commodo aliquet a quam. Pellentesque arcu velit, cursus et malesuada ut, consequat et diam. Nullam erat sem, rhoncus id ullamcorper vitae, rhoncus et arcu. In ultricies ultricies nulla, ut rutrum nisi iaculis at. Donec eu magna a metus ornare faucibus. Fusce aliquet faucibus ultricies. Morbi semper, est id tincidunt gravida, sem arcu adipiscing lacus, ac bibendum nulla leo eu purus. Quisque nec diam sed risus consectetur a ccumsan quis quis nibh. Vestibulum id purus lorem.</p>
  </div>
  <div class="letter letter__sign"><strong>Corin Maddox</strong>Co-Founder &amp; CEO</div>

  <div class="footer" style="height:14px">
    <div class="footer__grey" style="height:9px"></div>
    <div class="footer__blue" style="width:114px;height:14px;font-size:5px">www.sumvane-fs.com</div>
  </div>
</section>

<!-- Business card front -->
<section class="sheet card card--front" aria-label="Business card front">
  <div class="brand" style="left:13px;top:13px">
    <span class="brand__square" style="width:22px;height:22px"></span>
    <span class="brand__text"><span class="brand__name" style="font-size:14px">Sumvane</span><span class="brand__sub" style="font-size:3.8px">Financial Services</span></span>
  </div>
  <p class="card__name">Ardel Vinsk</p>
  <p class="card__role">Manager Director</p>
  <div class="card__rule"></div>
  <ul class="contact" style="left:13px;top:87px;font-size:4.6px;line-height:6.8px">
    <li><svg class="icon"><use href="#i-phone"/></svg>000-0000-0000</li>
    <li><svg class="icon"><use href="#i-mobile"/></svg>000-0000-0000</li>
    <li><svg class="icon"><use href="#i-mail"/></svg>info@sumvane-fs.com</li>
  </ul>
  <p class="card__address">Addres street, demo place<br>P.O. Box 000, 888 Avenue</p>
  <div class="footer" style="height:9px">
    <div class="footer__grey" style="height:5px"></div>
    <div class="footer__blue" style="width:86px;height:9px;font-size:4.6px;font-weight:700">www.sumvane-fs.com</div>
  </div>
</section>

<!-- Business card back -->
<section class="sheet card card--back" aria-label="Business card back">
  <div class="brand brand--white" style="left:54px;top:46px">
    <span class="brand__square" style="width:28px;height:28px"></span>
    <span class="brand__text"><span class="brand__name" style="font-size:18px">Sumvane</span><span class="brand__sub" style="font-size:4.6px">Financial Services</span></span>
  </div>
</section>
</body>
</html>
```